Benefit Porter

Need home page design for new website. The winner will have the opportunity to design the entire site.

I have attached 3 files.

1) Sort of a site map. PLEASE do not design the home page based on this wire frame. Be creative and use your expertise.

2) Tagline and Copy for the home page. Please just greek in or make up copy for areas that do not have copy at this time.

3) The logo.
Updates

Hi everyone, I am sorry for the delay. I have been out of town on unexpected business. I will make a decision this week. Thank you all for the great designs. Dale

```html
<!DOCTYPE html>
<html lang="en">
<head>
<meta charset="utf-8">
<title>Benefit Porter — Home</title>
<link href="https://fonts.googleapis.com/css2?family=Arimo:wght@400;700&family=Source+Sans+3:wght@400;600;700&display=swap" rel="stylesheet">
<style>
:root{
  --green:#3cb94a;
  --green-dark:#2a9a36;
  --blue:#1a6f9c;
  --blue-light:#2d8fc4;
  --ink:#1e1e1e;
  --body:#333;
  --rule:#e2e2e2;
  --footer:#2b2b2b;
  --footer-text:#b8b8b8;
  --caption-bg:rgba(40,40,40,.78);
}
*{margin:0;padding:0;box-sizing:border-box}
html,body{width:842px;height:1200px;overflow:hidden;background:#fff}
body{position:relative;font-family:"Arimo",sans-serif;color:var(--body)}
.abs{position:absolute}

/* header */
.site-header{left:0;top:0;width:842px;height:122px;background:linear-gradient(180deg,#d7e7f4 0%,#eef4fa 45%,#fff 80%)}
.brand{left:97px;top:24px;display:flex;align-items:center;gap:10px}
.brand-square{width:22px;height:22px;background:var(--ink)}
.brand-name{font-family:"Source Sans 3",sans-serif;font-weight:600;font-size:24px;color:var(--ink);line-height:1}
.main-nav{left:97px;top:96px;display:flex;font-size:10.5px;color:#333;text-transform:uppercase}
.main-nav span{padding:0 13px 0 10px;height:26px}
.main-nav .current{border-bottom:4px solid var(--blue)}

/* hero */
.hero{left:0;top:122px;width:842px;height:317px}
.hero-photo{position:absolute;inset:0;background:linear-gradient(160deg,#c7d9a8 0%,#7fa93e 35%,#5d8f26 70%,#4d7a1f 100%)}
.cta{width:164px;height:40px;border-radius:20px;color:#fff;font-family:"Source Sans 3",sans-serif;font-size:19px;display:flex;align-items:center;border:2px solid #fff;box-shadow:0 2px 4px rgba(0,0,0,.3)}
.cta-try{left:582px;top:84px;background:linear-gradient(180deg,var(--blue-light),var(--blue))}
.cta-demo{left:582px;top:142px;background:linear-gradient(180deg,#48c655,var(--green-dark))}
.cta-icon{width:40px;height:40px;margin-left:-2px;margin-right:12px;border-radius:50%;background:rgba(0,0,0,.2);border:2px solid #fff;display:flex;align-items:center;justify-content:center}
.cta strong{font-weight:700;margin-left:4px}
.hero-caption{left:97px;top:240px;width:647px;height:77px;background:var(--caption-bg);color:#fff;font-family:"Source Sans 3",sans-serif;font-size:24px;line-height:31px;padding:8px 14px}
.hero-caption b{color:var(--green);font-weight:700}
.slider-dots{left:773px;top:292px;display:flex;gap:3px}
.slider-dots i{width:11px;height:11px;border-radius:50%;background:#fff}
.slider-dots i.off{background:#c9ccd3}

/* feature cards */
.card{top:454px;width:205px;height:150px;border:1px solid #e4e4e4;border-top:5px solid var(--green);padding:12px 8px;font-size:9.4px;line-height:11.6px}
.card.dark{border-top-color:#333}
.card.blue{border-top-color:var(--blue)}
.card h3{font-family:"Source Sans 3",sans-serif;font-weight:400;font-size:18.5px;letter-spacing:-.3px;line-height:23px;color:var(--ink);margin-bottom:10px;white-space:nowrap}
.card.blue h3{white-space:normal}
.link{color:var(--blue);text-decoration:underline}
.link-green{color:var(--green);text-decoration:underline}

/* intro */
.section-title{font-family:"Source Sans 3",sans-serif;font-weight:400;font-size:21px;color:var(--ink)}
.intro-text{left:97px;top:666px;width:647px;font-size:10.9px;line-height:15px}
.btn{left:97px;top:707px;width:72px;height:28px;background:var(--green);color:#fff;font-size:11.5px;display:flex;align-items:center;justify-content:center;border:2px solid #fff;outline:1px solid #bfe5c3;border-radius:3px}
.rule{left:97px;width:647px;height:1px;background:var(--rule)}

/* news */
.news-item{top:814px;display:flex;gap:10px;font-size:9.6px;line-height:11.4px}
.news-date{color:var(--blue);text-align:center;width:22px}
.news-date b{display:block;font-family:"Source Sans 3",sans-serif;font-size:17px;line-height:16px}
.col-rule{top:768px;width:1px;height:134px;background:var(--rule)}

/* testimonials */
.testimonial{top:976px;display:flex;gap:10px;font-size:9.6px;line-height:11.4px}
.avatar{width:70px;height:62px;border:1px solid #ccc;background:linear-gradient(135deg,#e6cf9a,#d9a88c 55%,#c38a78)}
.testimonial h4{font-family:"Source Sans 3",sans-serif;font-weight:700;font-size:12.5px;color:var(--ink);margin-bottom:4px}

/* footer */
.site-footer{left:0;top:1114px;width:842px;height:86px;background:var(--footer);color:var(--footer-text);font-size:10px;text-align:center}
.footer-nav{margin-top:21px;word-spacing:2px}
.footer-nav span{margin:0 12px}
.copyright{margin-top:24px;font-size:9px;color:#8f8f8f}
</style>
</head>
<body>

<header class="abs site-header">
  <div class="abs brand"><span class="brand-square"></span><span class="brand-name">Benefit Porter</span></div>
  <nav class="abs main-nav">
    <span class="current">Pricing</span><span>Features</span><span>Services</span><span>Products</span><span>About</span><span>Contact</span>
  </nav>
</header>

<section class="abs hero">
  <div class="hero-photo" role="img" aria-label="Close-up of a golf putter and ball beside the hole on a green"></div>
  <div class="abs cta cta-try"><span class="cta-icon"><svg width="12" height="12" viewBox="0 0 12 12"><path d="M9 1 L2 6 L9 11 Z" fill="#fff"/></svg></span>Try for <strong>FREE</strong></div>
  <div class="abs cta cta-demo"><span class="cta-icon"><svg width="12" height="12" viewBox="0 0 12 12"><path d="M9 1 L2 6 L9 11 Z" fill="#fff"/></svg></span><strong>DEMO</strong>&nbsp;Here</div>
  <div class="abs hero-caption">We are experienced in both the art of <b>Fundraising</b> as well as the dynamics of a <b>Golf event</b></div>
  <div class="abs slider-dots"><i></i><i class="off"></i><i></i></div>
</section>

<article class="abs card" style="left:97px">
  <h3>Raise more, Stress Less</h3>
  <p>Charity golf events are proven to be an effective way to raise money for worthy causes. But who has the time to manage all the details? You do now, with BenefitPorter.<br><span class="link">Learn More</span></p>
</article>
<article class="abs card dark" style="left:318px">
  <h3>Everything you Need</h3>
  <p>We are experienced in both the art of fundraising as well as the dynamics of a golf event and we are here to help you. We offer everything from simple self-service tools that include professionally-designed website and email templates all the way up to full service event planning.<span class="link">Learn More</span></p>
</article>
<article class="abs card blue" style="left:539px">
  <h3>Sold! Silent Auction Moducle</h3>
  <p>Exclusive to BenefitPorter.com is our Silent Auction module. Through our partners we can add even more value to your golf event. Auction off premium items during the tournament and add to your fundraising!<br><span class="link">Learn More</span></p>
</article>

<h2 class="abs section-title" style="left:97px;top:633px">Charity Success, Minus the Stress</h2>
<p class="abs intro-text">Thinking about having a charity golf event but are turned off by the stress, hassle, and complexity – relax! BenefitPorter.com is your total solution for creating, managing, and successfully completing your event.</p>
<div class="abs btn">Learn more</div>

<div class="abs rule" style="top:757px"></div>

<h2 class="abs section-title" style="left:97px;top:772px">News &amp; Events</h2>
<div class="abs col-rule" style="left:314px"></div>
<div class="abs col-rule" style="left:545px"></div>
<div class="abs news-item" style="left:97px;width:200px">
  <div class="news-date"><b>25</b>sept.</div>
  <p>Praesent vestibulum aenean nonummy hendrerit mauris. Hasellus porta. Fusce suscipit varius mi. aenean nonummy hendrerit mauris. Hasellus porta. Fusce suscipit varius mi.</p>
</div>
<div class="abs news-item" style="left:333px;width:196px">
  <div class="news-date"><b>20</b>sept.</div>
  <p>Praesent vestibulum aenean nonummy hendrerit mauris. Hasellus porta. Fusce suscipit varius mi. aenean nonummy hendrerit mauris. Hasellus porta. Fusce suscipit varius mi.</p>
</div>
<div class="abs news-item" style="left:564px;width:182px">
  <div class="news-date"><b>15</b>sept.</div>
  <p>Praesent vestibulum aenean nonummy hendrerit mauris. Hasellus porta. Fusce suscipit varius mi. aenean nonummy hendrerit mauris. Hasellus porta. Fusce suscipit varius mi.</p>
</div>
<span class="abs link-green" style="left:710px;top:890px;font-size:9.6px">View all</span>

<div class="abs rule" style="top:914px"></div>

<h2 class="abs section-title" style="left:97px;top:930px">Testimonials</h2>
<div class="abs testimonial" style="left:97px;width:210px">
  <div class="avatar" role="img" aria-label="Portrait photo of Nora Whitfield"></div>
  <div style="width:128px"><h4>Nora Whitfield</h4><p>Dasenim ad minim vcipses labosam noase quid eytase eresa ea onsequatursuis autem vel.</p><span class="link-green">Learn more</span></div>
</div>
<div class="abs testimonial" style="left:335px;width:210px">
  <div class="avatar" role="img" aria-label="Portrait photo of Ella Marsh"></div>
  <div style="width:112px"><h4>Ella Marsh</h4><p>Dasenim ad minim vcipses labosam noase quid eytase eresa ea onsequatursuis autem vel.</p><span class="link-green">Learn more</span></div>
</div>
<div class="abs testimonial" style="left:554px;width:200px">
  <div class="avatar" role="img" aria-label="Portrait photo of Ella Marsh"></div>
  <div style="width:112px"><h4>Ella Marsh</h4><p>Dasenim ad minim vcipses labosam noase quid eytase eresa ea onsequatursuis autem vel.</p><span class="link-green">Learn more</span></div>
</div>
<span class="abs link" style="left:670px;top:1074px;font-size:9.6px">More Testimonials</span>

<footer class="abs site-footer">
  <div class="footer-nav"><span>Pricing</span>|<span>Features</span>|<span>Services</span>|<span>Products</span>|<span>About</span>|<span>Contact</span></div>
  <div class="copyright">Copyright 2014 www.benefitporter.com All Rights Reserved.</div>
</footer>

</body>
</html>
```